Résumé app needs 1 more template

Hi, I need 1 more template for my résumé app. The résumé app can be used in a browser (https://brightquill.com/resume-app) on an Koravo / Tabrix (https://apps.orvantel.com/app/id583726104) or on an Vellumos (https://market.tindrel.com/store/apps/details?id=com.brightquill.resume). The app lets the user create a résumé. It currently let's the user choose between 3 templates. I need 1 more. Please use the app first so you know how it will work.

Reason: Need more designs

Target Market(s)

Users of the app

Colors

Designer to choose colors to be used in the design.

Requirements
Must have
• original
• beautiful
• the resume template contains the data that the user can currently enter in the app (so do NOT design new features like sliders for level of experience etc)

```html
<!DOCTYPE html>
<html lang="en">
<head>
<meta charset="utf-8">
<title>Résumé Template – Blue Cards</title>
<link href="https://fonts.googleapis.com/css2?family=Montserrat:wght@300;400;500&display=swap" rel="stylesheet">
<style>
  :root {
    --accent: #27a9e1;
    --page: #f3f3f3;
    --card: #ffffff;
    --card-border: #8a8a8a;
    --text: #5a5a5a;
    --text-dark: #333333;
    --photo-fill: #f1f1f1;
    --white: #ffffff;
  }
  * { box-sizing: border-box; margin: 0; padding: 0; }
  html, body {
    width: 927px; height: 1200px; overflow: hidden;
    background: var(--white);
    font-family: "Montserrat", "Helvetica Neue", Arial, sans-serif;
    color: var(--text);
  }
  .resume { position: relative; width: 927px; height: 1200px; }
  .sheet {
    position: absolute; left: 27px; top: 27px; width: 873px; height: 1145px;
    background: var(--page); border-radius: 0 0 12px 12px;
  }
  .header-band {
    position: absolute; left: 27px; top: 27px; width: 873px; height: 191px;
    background: var(--accent);
  }
  .photo {
    position: absolute; left: 54px; top: 55px; width: 191px; height: 191px;
    background: var(--photo-fill); border: 1.5px solid var(--accent); border-radius: 10px;
  }
  .identity {
    position: absolute; left: 274px; top: 62px; width: 598px; text-align: center; color: var(--white);
  }
  .identity .name { font-size: 58px; font-weight: 500; line-height: 66px; letter-spacing: 1px; }
  .identity .rule { position: relative; height: 1px; background: rgba(255,255,255,.85); margin-top: 2px; }
  .identity .rule::before, .identity .rule::after {
    content: ""; position: absolute; top: -1.5px; width: 4px; height: 4px; border-radius: 50%; background: var(--white);
  }
  .identity .rule::before { left: -2px; }
  .identity .rule::after { right: -2px; }
  .identity .designation { font-size: 29px; font-weight: 300; letter-spacing: 1px; margin-top: 8px; }

  .card {
    position: absolute; background: var(--card);
    border: 1.2px solid var(--card-border); border-radius: 10px;
  }
  .card--contact { border-color: var(--accent); border-width: 1.5px; }
  .card-icon { position: absolute; left: 13px; }
  .card-title {
    position: absolute; left: 71px; font-size: 21px; font-weight: 500; color: var(--accent); letter-spacing: .3px;
  }
  .body-text { font-size: 14.2px; line-height: 21px; letter-spacing: .35px; font-weight: 400; }
  .summary-text { position: absolute; left: 19px; top: 82px; width: 460px; }
  .summary-text p + p { margin-top: 14px; }

  .contact-list { position: absolute; left: 15px; top: 80px; list-style: none; }
  .contact-list li { font-size: 17.5px; line-height: 34.5px; color: var(--text-dark); font-weight: 400; letter-spacing: .3px; }

  .entry-left { position: absolute; left: 19px; width: 195px; }
  .entry-divider { position: absolute; left: 240px; width: 1.2px; background: #666; }
  .entry-right { position: absolute; left: 255px; width: 530px; }
</style>
</head>
<body>
<main class="resume">
  <div class="sheet"></div>
  <header>
    <div class="header-band"></div>
    <div class="photo" role="img" aria-label="Profile photo placeholder"></div>
    <div class="identity">
      <h1 class="name">Your Name</h1>
      <div class="rule"></div>
      <p class="designation">Designation</p>
    </div>
  </header>

  <section class="card card--summary" style="left:54px; top:258px; width:532px; height:272px;">
    <svg class="card-icon" style="top:14px" width="45" height="39" viewBox="0 0 45 39" aria-hidden="true">
      <rect width="45" height="39" fill="#27a9e1"/>
      <rect x="8" y="7" width="29" height="3" fill="#fff"/>
      <rect x="8" y="14" width="29" height="3" fill="#fff"/>
      <rect x="8" y="21" width="29" height="3" fill="#fff"/>
      <rect x="8" y="28" width="20" height="3" fill="#fff"/>
    </svg>
    <h2 class="card-title" style="top:19px">Summary</h2>
    <div class="summary-text body-text">
      <p>Lorem Ipsum dummy texts was available for many years on adhesive sheets in different sizes and typefaces from a company called Glyphwell.</p>
      <p>When computers came along, Ordane included lorem ipsum in its SheetSmith publishing software, and you now see it wherever designers, content designers, art directors, user interface developers and web designer are at work.</p>
    </div>
  </section>

  <section class="card card--contact" style="left:600px; top:258px; width:272px; height:272px;">
    <svg class="card-icon" style="top:14px" width="42" height="40" viewBox="0 0 42 40" aria-hidden="true">
      <rect x="4" y="0" width="36" height="40" rx="2" fill="#27a9e1"/>
      <rect x="0" y="6" width="8" height="4" rx="2" fill="#27a9e1"/>
      <rect x="0" y="18" width="8" height="4" rx="2" fill="#27a9e1"/>
      <rect x="0" y="30" width="8" height="4" rx="2" fill="#27a9e1"/>
      <circle cx="23" cy="15" r="5" fill="#fff"/>
      <path d="M14 30 Q14 21 23 21 Q32 21 32 30 Z" fill="#fff"/>
    </svg>
    <h2 class="card-title" style="top:19px; left:65px">Contact Details</h2>
    <ul class="contact-list">
      <li>Street</li>
      <li>Postal Code</li>
      <li>City</li>
      <li>Phone</li>
      <li>Email</li>
    </ul>
  </section>

  <section class="card card--experience" style="left:54px; top:545px; width:818px; height:190px;">
    <svg class="card-icon" style="top:15px" width="46" height="36" viewBox="0 0 46 36" aria-hidden="true">
      <path d="M16 6 V2 H30 V6" fill="none" stroke="#27a9e1" stroke-width="3"/>
      <rect x="0" y="6" width="46" height="30" rx="2" fill="#27a9e1"/>
      <rect x="0" y="17" width="46" height="1.5" fill="#fff"/>
      <rect x="20" y="15" width="6" height="5" fill="#fff"/>
    </svg>
    <h2 class="card-title" style="top:21px">Experience</h2>
    <p class="entry-left body-text" style="top:71px">Lorem Ipsum dummy texts was available for many years on adhesive sheets.</p>
    <div class="entry-divider" style="top:66px; height:109px"></div>
    <p class="entry-right body-text" style="top:71px">When computers came along, Ordane included lorem ipsum in its SheetSmith publishing software, content designers, art directors, user interface developers and web designer are at work.</p>
  </section>

  <section class="card card--education" style="left:54px; top:749px; width:818px; height:190px;">
    <svg class="card-icon" style="top:11px; left:10px" width="48" height="28" viewBox="0 0 48 28" aria-hidden="true">
      <path d="M0 12 L24 2 L48 12 L24 22 Z" fill="#27a9e1"/>
      <path d="M12 16 V24 Q24 30 36 24 V16 L24 21 Z" fill="#27a9e1"/>
    </svg>
    <h2 class="card-title" style="top:14px">Education</h2>
    <p class="entry-left body-text" style="top:61px">Lorem Ipsum dummy texts was available for many years on adhesive sheets.</p>
    <div class="entry-divider" style="top:55px; height:110px"></div>
    <p class="entry-right body-text" style="top:61px">When computers came along, Ordane included lorem ipsum in its SheetSmith publishing software, content designers, art directors, user interface developers and web designer are at work.</p>
  </section>

  <section class="card card--others" style="left:54px; top:954px; width:818px; height:190px;">
    <svg class="card-icon" style="top:11px; left:14px" width="44" height="44" viewBox="0 0 44 44" aria-hidden="true">
      <path d="M0 6 L38 0 L40 8 L4 14 Z" fill="#27a9e1"/>
      <rect x="4" y="8" width="38" height="34" fill="#27a9e1"/>
      <rect x="9" y="13" width="28" height="24" fill="none" stroke="#fff" stroke-width="2.5"/>
    </svg>
    <h2 class="card-title" style="top:23px">Others</h2>
    <p class="entry-left body-text" style="top:70px">Lorem Ipsum dummy texts was available for many years on adhesive sheets.</p>
    <div class="entry-divider" style="top:65px; height:109px"></div>
    <p class="entry-right body-text" style="top:70px">When computers came along, Ordane included lorem ipsum in its SheetSmith publishing software, content designers, art directors, user interface developers and web designer are at work.</p>
  </section>
</main>
</body>
</html>
```